Coral Ridge Networks Ltd

I need a website that is an informational only. We are a construction business building telecommunications sites. Seeing how our company is Coral Ridge the color blue might want to be incorporated in the color scheme.
I can provide more picture of towers and wireless communications if needed.
current website www.coralridgenet.ca

Industry/Entity Type

Wireless Telecommunications, Construction

Coding

Coded - Design and coding required

Number of Pages Required

2 page

Font styles to use
Sans Serif

Colors

Designer to choose colors to be used in the design.

```html
<!DOCTYPE html>
<html lang="en">
<head>
<meta charset="utf-8">
<title>Coral Ridge Networks Ltd</title>
<link href="https://fonts.googleapis.com/css2?family=Lato:wght@700;900&family=Poppins:wght@400;500;600&display=swap" rel="stylesheet">
<style>
:root{
  --navy:#283a8f;
  --navy-dark:#1f2d70;
  --sky:#5ea8e2;
  --ink:#1b1b1f;
  --text:#6b6f78;
  --line:#e3e5ea;
  --card:#ffffff;
  --soft:#efeff1;
  --footer:#2a2d33;
}
*{box-sizing:border-box;margin:0;padding:0}
html,body{width:1200px;height:4057px;overflow:hidden}
body{font-family:'Poppins',sans-serif;color:var(--ink);background:#fff;position:relative}
.abs{position:absolute}
h1,h2,h3,h4{font-family:'Lato',sans-serif;font-weight:900}
.topbar{top:0;left:0;width:1200px;height:43px;background:var(--navy);color:#fff;font-size:13px;font-weight:500;padding:0 85px;display:flex;align-items:center;justify-content:space-between}
.social-mini{display:flex;gap:14px}
.social-mini span{width:16px;height:16px;border-radius:50%;background:#fff;display:block}
.header{top:43px;left:0;width:1200px;height:133px;background:#fff}
.brand{font-family:'Poppins',sans-serif;font-weight:600;color:var(--navy);display:flex;align-items:center;gap:10px}
.brand i{width:14px;height:14px;background:var(--sky);display:block;border-radius:50%}
.header .brand{left:85px;top:46px;font-size:22px;line-height:1.05;width:200px}
.hinfo{top:26px;display:flex;align-items:center;gap:18px;font-size:12.5px}
.hinfo b{display:block;font-size:15px;font-weight:600;margin-bottom:2px}
.ico{width:38px;height:38px;border-radius:50%;background:var(--soft);display:flex;align-items:center;justify-content:center;flex:none}
.vsep{top:16px;width:1px;height:62px;background:var(--line)}
.hero{top:176px;left:0;width:1200px;height:704px;background:linear-gradient(180deg,#4e5460 0%,#5f6368 45%,#4a4c50 100%)}
.nav{top:148px;left:85px;width:1028px;height:57px;background:var(--navy);display:flex;align-items:center;padding-left:33px;gap:38px;color:#fff;font-size:14px;z-index:3}
.nav .active{font-weight:600}
.nav .search{position:absolute;right:160px;top:18px}
.nav .cta{position:absolute;right:0;top:0;width:129px;height:57px;background:var(--sky);display:flex;align-items:center;justify-content:center;font-weight:600;font-size:14px}
.hero-text{top:350px;left:0;width:1200px;text-align:center;color:#fff}
.hero-text .eyebrow{color:var(--sky);font-size:15px;font-weight:500}
.hero-text h1{font-size:70px;line-height:78px;margin-top:14px}
.hero-text p{font-size:16px;line-height:23px;width:500px;margin:22px auto 0}
.btn{display:inline-flex;align-items:center;justify-content:center;gap:10px;font-size:14px;font-weight:600;border-radius:2px}
.hero-btns{top:633px;left:458px;display:flex;gap:20px}
.hero-btns .btn{height:51px;width:130px}
.b-navy{background:var(--navy);color:#fff}
.b-white{background:#fff;color:var(--navy)}
.diamond{top:830px;left:564px;width:72px;height:72px;background:#fff;transform:rotate(45deg);box-shadow:0 6px 16px rgba(0,0,0,.08)}
.section-head{left:0;width:1200px;text-align:center}
.eyebrow-b{color:var(--navy);font-size:15px;font-weight:500}
.section-head h2{font-size:40px;margin-top:6px}
.card{top:1125px;width:328px;height:379px;background:var(--card);border:1px solid var(--line);padding:26px 26px}
.card .iconbox{width:86px;height:80px;background:var(--soft);display:flex;align-items:center;justify-content:center}
.card .num{position:absolute;right:34px;top:42px;font-family:'Poppins',sans-serif;font-size:44px;color:#c8ccd4;font-weight:400}
.card h3{font-size:25px;color:var(--navy);margin-top:24px;font-weight:700}
.card p{font-size:12.5px;line-height:20.5px;color:#3a3d44;margin-top:14px;width:270px}
.card .btn{position:absolute;left:26px;top:298px;width:145px;height:38px}
.b-grey{background:var(--soft);color:var(--ink)}
.cardbar{top:1504px;height:16px}
.why-text{top:1630px;left:85px;width:500px}
.why-text h2{font-size:40px;line-height:44px;margin-top:10px}
.why-text p{font-size:12.8px;line-height:22px;color:var(--text);margin-top:14px}
.why-text ul{list-style:none;margin-top:22px}
.why-text li{font-size:12.8px;font-weight:500;line-height:30px;display:flex;align-items:center;gap:12px}
.why-photo{top:1683px;left:651px;width:462px;height:462px;border-radius:50%;background:radial-gradient(circle at 45% 40%,#7a8fb8,#3f5684 60%,#2e3f66)}
.why-badge{top:1641px;left:954px;width:158px;height:158px;border-radius:50%;background:#fff;display:flex;align-items:center;justify-content:center;box-shadow:0 4px 16px rgba(0,0,0,.1)}
.why-badge .brand{font-size:20px;text-align:center;flex-direction:column;gap:6px}
.about{top:2268px;left:0;width:1200px;height:718px;background:linear-gradient(120deg,#26313b,#3b4650 55%,#2f363e)}
.about-art{top:2315px;left:157px;width:284px;height:520px;background:radial-gradient(ellipse at 50% 45%,#3f9e79 0%,#2d6b5a 45%,rgba(45,60,70,0) 75%)}
.about-text{top:2380px;left:524px;width:580px;color:#fff}
.about-text .eyebrow{font-size:14px;font-weight:500}
.about-text h2{font-size:38px;margin-top:8px}
.about-text p{font-size:12.8px;line-height:22px;margin-top:14px;color:#e6e8ec}
.about-text .btn{margin-top:22px;width:156px;height:53px;border:1px solid #fff;color:#fff}
.contact{top:2833px;left:85px;width:1028px;height:523px;background:#fff;border:1px solid var(--line);box-shadow:0 6px 20px rgba(0,0,0,.05)}
.contact h2{position:absolute;top:54px;width:100%;text-align:center;font-size:38px}
.contact .sub{position:absolute;top:120px;width:100%;text-align:center;font-size:13px;line-height:22px;color:var(--text)}
.field{position:absolute;top:196px;width:294px;border-bottom:1px solid var(--line);font-size:13px;color:#8f939b;padding-bottom:12px}
.field.msg{top:281px;left:56px;width:914px;height:92px}
.contact .btn{position:absolute;left:449px;top:402px;width:132px;height:52px}
.footer{top:3473px;left:0;width:1200px;height:584px;background:linear-gradient(180deg,#2b3038,#3a3d42 50%,#2a2d31)}
.flogo{top:3473px;left:85px;width:221px;height:121px;background:#fff;display:flex;align-items:center;justify-content:center}
.flogo .brand{font-size:22px;flex-direction:column;gap:6px;text-align:center}
.fstrip{top:3473px;left:348px;width:765px;height:121px;background:#ececee;border-radius:0 0 6px 6px}
.fstrip .hinfo{top:38px}
.fstrip .vsep{top:22px;height:76px;background:#d3d5da}
.fcol{top:3668px;color:#fff}
.fcol h4{font-size:21px;font-weight:700;margin-bottom:24px}
.fcol p{font-size:12.8px;line-height:22px;width:235px}
.fcol a{display:block;font-size:12.5px;font-weight:500;line-height:35px;color:#fff;text-decoration:none}
.fsocial{top:3848px;left:85px;display:flex;gap:12px}
.fsocial span{width:45px;height:45px;border-radius:50%;background:#fff;display:block}
.map{top:3726px;left:876px;width:237px;height:183px;background:linear-gradient(135deg,#dfe8d8,#e9ede4 50%,#d6e2cf);border:2px solid #fff}
.fline{top:3967px;left:85px;width:1028px;height:1px;background:#5a5e66}
.fbottom{top:3987px;left:85px;width:1028px;display:flex;justify-content:space-between;color:#fff;font-size:12.5px}
.fbottom em{font-style:normal;color:var(--sky)}
</style>
</head>
<body>

<div class="abs topbar"><span>Coral Ridge Networks Ltd</span><div class="social-mini"><span></span><span></span><span></span></div></div>

<header class="abs header">
  <div class="abs brand"><i></i>Coral Ridge</div>
  <div class="abs hinfo" style="left:418px"><span class="ico"><svg width="16" height="16" viewBox="0 0 24 24" fill="none" stroke="#8a8f99" stroke-width="1.8"><path d="M5 3h4l2 5-3 2a12 12 0 0 0 6 6l2-3 5 2v4a2 2 0 0 1-2 2A17 17 0 0 1 3 5a2 2 0 0 1 2-2z"/></svg></span><div><b>Call Us:</b>1-604-555-0142</div></div>
  <div class="abs vsep" style="left:618px"></div>
  <div class="abs hinfo" style="left:658px"><span class="ico"><svg width="16" height="16" viewBox="0 0 24 24" fill="none" stroke="#8a8f99" stroke-width="1.8"><rect x="3" y="5" width="18" height="14"/><path d="M3 6l9 7 9-7"/></svg></span><div><b>Email:</b>info@coralridgenet.ca</div></div>
  <div class="abs vsep" style="left:890px"></div>
  <div class="abs hinfo" style="left:930px;top:20px"><span class="ico"><svg width="16" height="16" viewBox="0 0 24 24" fill="none" stroke="#8a8f99" stroke-width="1.8"><path d="M12 21s-7-7-7-12a7 7 0 0 1 14 0c0 5-7 12-7 12z"/><circle cx="12" cy="9" r="2.5"/></svg></span><div style="line-height:21px"><b>Location:</b>4150 Harbour Rd<br>Surrey, BC V3S 1A1</div></div>
</header>

<div class="abs hero" role="img" aria-label="Rooftop telecommunication antennas with city and mountains behind"></div>
<svg class="abs" style="top:800px;left:0" width="1200" height="82" viewBox="0 0 1200 82"><path d="M0 26 Q600 110 1200 26 L1200 82 L0 82Z" fill="#fff"/></svg>

<nav class="abs nav"><span class="active">Home</span><span>Services</span><span>About</span><span>Why Choose Us</span><span>Contact Us</span>
  <svg class="search" width="22" height="22" viewBox="0 0 24 24" fill="none" stroke="#fff" stroke-width="1.8"><circle cx="10" cy="10" r="7"/><path d="M15 15l6 6"/></svg>
  <span class="cta">Get Started</span></nav>

<div class="abs hero-text">
  <div class="eyebrow">WELCOME TO</div>
  <h1>Coral Ridge<br>Networks Ltd</h1>
  <p>Our courteous, professional team is able to support a range of services to meet your requirements.</p>
</div>
<div class="abs hero-btns"><span class="btn b-navy">Learn More</span><span class="btn b-white">Contact Now</span></div>

<div class="abs diamond"></div>
<svg class="abs" style="top:852px;left:590px" width="20" height="30" viewBox="0 0 20 30" fill="none" stroke="#283a8f" stroke-width="1.8"><path d="M10 2v25M2 19l8 8 8-8"/></svg>

<svg class="abs" style="top:946px;left:390px" width="420" height="180" viewBox="0 0 420 180"><path d="M20 180 A190 190 0 0 1 400 180" fill="none" stroke="#f1f1f3" stroke-width="36"/></svg>
<div class="abs section-head" style="top:1024px"><div class="eyebrow-b">SERVICES WE PROVIDE</div><h2>Explore Our Services</h2></div>

<div class="abs card" style="left:85px"><div class="iconbox"><svg width="40" height="44" viewBox="0 0 40 44" fill="none" stroke="#283a8f" stroke-width="1.6"><circle cx="20" cy="12" r="3"/><path d="M13 6a10 10 0 0 0 0 12M27 6a10 10 0 0 1 0 12M20 15L12 42M20 15l8 27M15 32h10"/></svg></div><span class="num">01</span><h3>Rooftop Sites</h3><p>Structural upgrades or simple ballast mounts. Shelter on the ground, leasehold build outs or cabinets on the roof. Coral Ridge can install what you need where you need it.</p><span class="btn b-navy">Read More <svg width="16" height="10" viewBox="0 0 16 10" fill="none" stroke="currentColor" stroke-width="1.5"><path d="M0 5h14M10 1l4 4-4 4"/></svg></span></div>
<div class="abs cardbar" style="left:112px;width:272px;background:var(--navy)"></div>

<div class="abs card" style="left:436px"><div class="iconbox"><svg width="40" height="44" viewBox="0 0 40 44" fill="none" stroke="#283a8f" stroke-width="1.6"><path d="M20 4v38M14 42l6-24 6 24M8 14h24M10 10v8M30 10v8"/></svg></div><span class="num">02</span><h3>Towers and Monopoles</h3><p>Coral Ridge can engineer, supply and install all your tower needs. New structures or existing, call us for pricing we would be happy to help out.</p><span class="btn b-grey">Read More <svg width="16" height="10" viewBox="0 0 16 10" fill="none" stroke="currentColor" stroke-width="1.5"><path d="M0 5h14M10 1l4 4-4 4"/></svg></span></div>
<div class="abs cardbar" style="left:463px;width:272px;background:var(--soft)"></div>

<div class="abs card" style="left:787px"><div class="iconbox"><svg width="40" height="44" viewBox="0 0 40 44" fill="none" stroke="#283a8f" stroke-width="1.6"><rect x="8" y="4" width="18" height="38"/><path d="M12 10h3M19 10h3M12 16h3M19 16h3M12 22h3M19 22h3"/><circle cx="30" cy="34" r="6"/></svg></div><span class="num">03</span><h3>In Building</h3><p>Small office or large Hotel. Coral Ridge has installed services into all size buildings. Fiber, cat6, or coax, we have the abilities to install, test, and get the job done.</p><span class="btn b-grey">Read More <svg width="16" height="10" viewBox="0 0 16 10" fill="none" stroke="currentColor" stroke-width="1.5"><path d="M0 5h14M10 1l4 4-4 4"/></svg></span></div>
<div class="abs cardbar" style="left:814px;width:272px;background:var(--soft)"></div>

<div class="abs why-text">
  <div class="eyebrow-b">WHY CHOOSE US</div>
  <h2>Coral Ridge<br>Networks Ltd</h2>
  <p>At Coral Ridge Networks Ltd Safety is number one. Coral Ridge Ltd is committed to a strong safety policy, protecting its staff and the general public from accidents and harm. All Coral Ridge Employees are certified "Tower Competent Climber and Rescue".</p>
  <p>In addition to tower safety and fall protection Coral Ridge's safety training and practices include but are not limited to the following:</p>
  <ul>
    <li><svg width="14" height="12" viewBox="0 0 14 12" fill="none" stroke="#283a8f" stroke-width="1.6"><path d="M1 6l4 4 8-9"/></svg>COR Certified</li>
    <li><svg width="14" height="12" viewBox="0 0 14 12" fill="none" stroke="#283a8f" stroke-width="1.6"><path d="M1 6l4 4 8-9"/></svg>BC Level 1 first aid</li>
    <li><svg width="14" height="12" viewBox="0 0 14 12" fill="none" stroke="#283a8f" stroke-width="1.6"><path d="M1 6l4 4 8-9"/></svg>Transportation Endorsement first aid</li>
    <li><svg width="14" height="12" viewBox="0 0 14 12" fill="none" stroke="#283a8f" stroke-width="1.6"><path d="M1 6l4 4 8-9"/></svg>Sprat Level 1</li>
    <li><svg width="14" height="12" viewBox="0 0 14 12" fill="none" stroke="#283a8f" stroke-width="1.6"><path d="M1 6l4 4 8-9"/></svg>On site tailboard meeting with daily checklist sign off and picture</li>
    <li><svg width="14" height="12" viewBox="0 0 14 12" fill="none" stroke="#283a8f" stroke-width="1.6"><path d="M1 6l4 4 8-9"/></svg>documentation</li>
    <li><svg width="14" height="12" viewBox="0 0 14 12" fill="none" stroke="#283a8f" stroke-width="1.6"><path d="M1 6l4 4 8-9"/></svg>Monthly in office safety meetings</li>
    <li><svg width="14" height="12" viewBox="0 0 14 12" fill="none" stroke="#283a8f" stroke-width="1.6"><path d="M1 6l4 4 8-9"/></svg>Job site specific hazard assessment and reporting</li>
  </ul>
</div>
<div class="abs why-photo" role="img" aria-label="Lattice telecom tower with antennas and a dish against a blue sky"></div>
<div class="abs why-badge"><div class="brand"><i></i>Coral Ridge</div></div>

<section class="abs about" role="img" aria-label="Crane and work crew setting up equipment on a city street"></section>
<div class="abs about-art" role="img" aria-label="Illustration of a glowing green signal tower"></div>
<div class="abs about-text">
  <div class="eyebrow">ABOUT US</div>
  <h2>Some Words About Us</h2>
  <p>At <b>Coral Ridge Ltd</b>, we are dedicated to providing our customers with friendly professional service. We value your business. We have made it our mission to provide reliable products and services in our customer-driven approach.</p>
  <p style="margin-top:10px">Our courteous, professional team is able to support a range of services to meet your requirements.</p>
  <p style="margin-top:10px">To learn more about <b>Coral Ridge Ltd</b>, and the products and services we can offer, please call us at <b>1-604-555-0142.</b></p>
  <span class="btn">Read More <svg width="16" height="10" viewBox="0 0 16 10" fill="none" stroke="currentColor" stroke-width="1.5"><path d="M0 5h14M10 1l4 4-4 4"/></svg></span>
</div>

<div class="abs contact">
  <h2>Contact Us</h2>
  <div class="sub">We guarantee high-quality customer support service with high-speed<br>satellite connection all over the world</div>
  <div class="field" style="left:56px">Name</div>
  <div class="field" style="left:366px">Email</div>
  <div class="field" style="left:676px">Phone</div>
  <div class="field msg">Please tell us your feedback</div>
  <span class="btn b-navy">Submit Form</span>
</div>

<footer class="abs footer" role="img" aria-label="Dark blurred photo of a telecom tower at dusk"></footer>
<div class="abs flogo"><div class="brand"><i></i>Coral Ridge</div></div>
<div class="abs fstrip">
  <div class="abs hinfo" style="left:32px"><span class="ico" style="background:#fff"><svg width="16" height="16" viewBox="0 0 24 24" fill="none" stroke="#8a8f99" stroke-width="1.8"><path d="M5 3h4l2 5-3 2a12 12 0 0 0 6 6l2-3 5 2v4a2 2 0 0 1-2 2A17 17 0 0 1 3 5a2 2 0 0 1 2-2z"/></svg></span><div><b>Call Us:</b>1-604-555-0142</div></div>
  <div class="abs vsep" style="left:234px"></div>
  <div class="abs hinfo" style="left:274px"><span class="ico" style="background:#fff"><svg width="16" height="16" viewBox="0 0 24 24" fill="none" stroke="#8a8f99" stroke-width="1.8"><rect x="3" y="5" width="18" height="14"/><path d="M3 6l9 7 9-7"/></svg></span><div><b>Email:</b>info@coralridgenet.ca</div></div>
  <div class="abs vsep" style="left:508px"></div>
  <div class="abs hinfo" style="left:548px;top:30px"><span class="ico" style="background:#fff"><svg width="16" height="16" viewBox="0 0 24 24" fill="none" stroke="#8a8f99" stroke-width="1.8"><path d="M12 21s-7-7-7-12a7 7 0 0 1 14 0c0 5-7 12-7 12z"/><circle cx="12" cy="9" r="2.5"/></svg></span><div style="line-height:21px"><b>Location:</b>4150 Harbour Rd<br>Surrey, BC V3S 1A1</div></div>
</div>

<div class="abs fcol" style="left:85px"><h4>About Us</h4><p>Our courteous, professional team is able to support a range of services to meet your requirements.</p></div>
<div class="abs fsocial"><span></span><span></span><span></span></div>
<div class="abs fcol" style="left:438px"><h4>Main Menu</h4><a>Home</a><a>Services</a><a>About</a><a>Why Choose Us</a><a>Contact Us</a></div>
<div class="abs fcol" style="left:647px"><h4>Our Services</h4><a>Rooftop Sites</a><a>Towers and Monopoles</a><a>In Building</a></div>
<div class="abs fcol" style="left:876px"><h4>Location</h4></div>
<div class="abs map" role="img" aria-label="Street map showing the office location"></div>

<div class="abs fline"></div>
<div class="abs fbottom"><span>Privacy Policy &nbsp;&bull;&nbsp; Term and Condition</span><span>Copyright 2017 <em>Coral Ridge Ltd</em></span></div>

</body>
</html>
```